Business Card design for construction company

I would like a business card design for a construction company - Harlow Constructions. I have attached the ai logo file for use. I would like the card to be very smart and clean and incorporate only white and the two colours in the logo. I would like the card to have two sides. One side can just have the logo, the other with the relevant information.

Target Market(s)

Building and Construction Clients

Industry/Entity Type

Business

Contact Information for Business Card

Name: Tom Pardoe
Company: Harlow Constructions Pty Limited
Address: 14 Mallee Crescent Carrow Vale 2093
Phone: 0427 531 068
Email: tomp@harlowbuild-example.com.au

Font styles to use
Serif
Sans Serif

Requirements
Must have
• Details noted above
• Logo as provided
• Colours as in logo
• Square edges
• A font that compliments the logo
Should not have
• Any colour other than white and those in logo
• Rounded edges

```html
<!DOCTYPE html>
<html lang="en">
<head>
<meta charset="utf-8">
<title>Harlow Constructions – Business Card</title>
<link rel="stylesheet" href="https://fonts.googleapis.com/css2?family=Poppins:wght@300;400;600&display=swap">
<style>
  :root {
    --brand-grey: #595a5c;
    --brand-blue: #1ba6e0;
    --text-grey: #3c3d3f;
    --rule-grey: #555658;
    --paper: #ffffff;
  }
  * { box-sizing: border-box; margin: 0; padding: 0; }
  html, body {
    width: 1200px;
    height: 311px;
    overflow: hidden;
    background: var(--paper);
    font-family: "Poppins", sans-serif;
  }
  .canvas {
    position: relative;
    width: 1200px;
    height: 311px;
  }
  .card-front {
    position: absolute;
    left: 0;
    top: 0;
    width: 540px;
    height: 310px;
    background: var(--brand-grey);
    display: flex;
    align-items: center;
    justify-content: center;
  }
  .brand-name {
    color: var(--paper);
    font-weight: 400;
    font-size: 21px;
    letter-spacing: 3px;
    text-transform: uppercase;
  }
  .card-back {
    position: absolute;
    left: 659px;
    top: 1px;
    width: 537px;
    height: 309px;
    border: 2px solid var(--rule-grey);
    background: var(--paper);
  }
  .holder-name {
    position: absolute;
    right: 357px;
    top: 137px;
    font-size: 21px;
    font-weight: 300;
    color: var(--text-grey);
    white-space: nowrap;
  }
  .holder-name .given {
    color: var(--brand-blue);
    font-weight: 600;
  }
  .divider {
    position: absolute;
    left: 199px;
    top: 89px;
    width: 2px;
    height: 130px;
    background: var(--rule-grey);
  }
  .contact-list {
    position: absolute;
    left: 220px;
    top: 113px;
    list-style: none;
  }
  .contact-item {
    display: flex;
    align-items: center;
    height: 31px;
    font-size: 13.5px;
    font-weight: 300;
    color: var(--text-grey);
  }
  .contact-icon {
    width: 20px;
    height: 22px;
    margin-right: 15px;
    flex: none;
  }
  .contact-icon * {
    fill: none;
    stroke: var(--brand-blue);
    stroke-width: 1.4;
  }
</style>
</head>
<body>
<div class="canvas">
  <section class="card-front">
    <span class="brand-name">Harlow Constructions</span>
  </section>

  <section class="card-back">
    <p class="holder-name"><span class="given">TOM</span> Pardoe</p>
    <div class="divider"></div>
    <ul class="contact-list">
      <li class="contact-item">
        <svg class="contact-icon" viewBox="0 0 20 22" aria-hidden="true">
          <rect x="4" y="1" width="12" height="20" rx="2"/>
          <line x1="4" y1="4.5" x2="16" y2="4.5"/>
          <line x1="4" y1="17" x2="16" y2="17"/>
        </svg>
        0427 531 068
      </li>
      <li class="contact-item">
        <svg class="contact-icon" viewBox="0 0 20 22" aria-hidden="true">
          <circle cx="10" cy="11" r="3.5"/>
          <path d="M13.5 8v4.5c0 2 3 2 3-1A7 7 0 1 0 13 17"/>
        </svg>
        tomp@harlowbuild-example.com.au
      </li>
      <li class="contact-item">
        <svg class="contact-icon" viewBox="0 0 20 22" aria-hidden="true">
          <path d="M10 21C5 15 3 12 3 8.5a7 7 0 0 1 14 0C17 12 15 15 10 21z"/>
          <circle cx="10" cy="8.5" r="2.8"/>
        </svg>
        14 Mallee Crescent Carrow Vale 2093
      </li>
    </ul>
  </section>
</div>
</body>
</html>
```